High end Electrical/home automation Business Card

Need a card for a high end electrical and home automation company utilising the existing logo.
Phone
Email
Website

Like black look with raised detail. Don’t necessarily need to keep colour of logo it could be made grayscale or white etc

Target Market(s)

High end clients

Contact Information for Business Card

Ridgeline Electrical

Requirements
Must have
• Logo, phone, email, website, address

High end look
Nice to have
• Black background card
Raised font
Should not have
• Lots of colour

```html
<!DOCTYPE html>
<html lang="en">
<head>
<meta charset="utf-8">
<title>Ridgeline Electrical – Business Card</title>
<link href="https://fonts.googleapis.com/css2?family=Lato:wght@400;700&display=swap" rel="stylesheet">
<style>
  :root {
    --page: #e4e4e4;
    --card: #232326;
    --card-pattern: #28282b;
    --blue: #0a8fd6;
    --white: #f2f2f2;
    --silver: #b9b9bc;
  }
  * { margin: 0; padding: 0; box-sizing: border-box; }
  html, body {
    width: 1200px; height: 1200px; overflow: hidden;
    background: var(--page);
    font-family: "Lato", Arial, sans-serif;
  }
  .card {
    position: absolute;
    left: 257px;
    width: 686px; height: 392px;
    background: var(--card);
    overflow: hidden;
  }
  .card--front { top: 165px; }
  .card--back { top: 653px; }

  /* front */
  .brand-mark {
    position: absolute; left: 34px; top: 120px;
    color: var(--silver);
    font-weight: 700; font-size: 52px; line-height: 1.05;
    letter-spacing: 0.5px;
  }
  .accent-bar {
    position: absolute; right: 0; top: 178px;
    width: 18px; height: 42px; background: var(--blue);
  }
  .holder {
    position: absolute; right: 43px; top: 178px; text-align: right;
  }
  .holder__name {
    color: var(--blue); font-weight: 700; font-size: 26px;
    line-height: 1; letter-spacing: 0.3px;
  }
  .holder__title {
    color: var(--white); font-weight: 700; font-size: 17px; margin-top: 2px;
  }
  .address {
    position: absolute; right: 43px; top: 242px; text-align: right;
    color: var(--white); font-size: 16px; line-height: 19.5px;
  }
  .contacts {
    position: absolute; right: 38px; top: 313px; list-style: none;
    color: var(--white); font-size: 16px; line-height: 19.5px;
  }
  .contacts li { display: flex; justify-content: flex-end; align-items: center; gap: 10px; }
  .contacts svg { width: 12px; height: 12px; fill: var(--blue); }

  /* back */
  .pattern-field {
    position: absolute; inset: 0; background: var(--card-pattern);
  }
  .back-brand {
    position: absolute; left: 0; right: 0; top: 232px;
    display: flex; justify-content: center; align-items: center; gap: 12px;
  }
  .back-brand__dot {
    width: 22px; height: 22px; border-radius: 50%; background: var(--blue);
  }
  .back-brand__name {
    color: var(--white); font-weight: 700; font-size: 36px; letter-spacing: -0.3px;
  }
  .back-web {
    position: absolute; left: 0; right: 0; top: 318px; text-align: center;
    color: var(--white); font-size: 16px; letter-spacing: 3.6px;
  }
</style>
</head>
<body>
  <section class="card card--front">
    <div class="brand-mark">Ridgeline<br>Electrical</div>
    <div class="accent-bar"></div>
    <div class="holder">
      <div class="holder__name">DANIEL HARTLEY</div>
      <div class="holder__title">President</div>
    </div>
    <div class="address">
      Ridgeline Electrical LLC<br>
      2140 Alder Crest Road<br>
      Juneau, Alaska 99801
    </div>
    <ul class="contacts">
      <li>482-330-7164
        <svg viewBox="0 0 24 24"><path d="M6.6 10.8a15.1 15.1 0 0 0 6.6 6.6l2.2-2.2c.3-.3.7-.4 1-.2 1.1.4 2.3.6 3.6.6.6 0 1 .4 1 1V20c0 .6-.4 1-1 1A17 17 0 0 1 3 4c0-.6.4-1 1-1h3.5c.6 0 1 .4 1 1 0 1.3.2 2.5.6 3.6.1.3 0 .7-.2 1z"/></svg>
      </li>
      <li>info@ridgelineelectrical.com
        <svg viewBox="0 0 24 24"><path d="M2 5h20v14H2z M2 5l10 8 10-8" stroke="#232326" stroke-width="1.5"/></svg>
      </li>
      <li>www.ridgelineelectrical.com
        <svg viewBox="0 0 24 24"><circle cx="12" cy="12" r="10"/></svg>
      </li>
    </ul>
  </section>

  <section class="card card--back">
    <div class="pattern-field" role="img" aria-label="Faint repeating brand pattern across the card"></div>
    <div class="back-brand">
      <span class="back-brand__dot"></span>
      <span class="back-brand__name">Ridgeline Electrical</span>
    </div>
    <div class="back-web">www.ridgelineelectrical.com</div>
  </section>
</body>
</html>
```